Website design for luxury private hair salon

I'm looking for someone to use my Logo and build me a website for my webpage www.lunetresses.com.au (You can have a look at it as it has every detail I need included on it already), however I want a fresh new appearance and it to look and feel super stylish.

I am thinking colours in black, with silver or white, beautiful hair images like the ones you'll see on the current webpage - the price list as per what you already see.

I will include a copy of my biz card on here, so you can see the feel of the card, and design a website with a similar feel. It is matt black with a foil silver.

Modern, but classic and fresh. I will also need you to be able to publish it to my URL for me as I have no idea how to do this. I need it up and running pronto!

The website will need to be able to be read clearly on all devices incluing smart phones and ipads. The URL is currently registered and hosted by Nimbo Vault

Thinking a Home Page - large logo etc and write up on who and what we offer
Services/Price List page - as per the price list on my current webpage
Contact Page - with a built in contact form.

Target Market(s)

Middle aged, fashionable, stylish women and men who enjoy luxury hair care and styling in an upmarket location.

Industry/Entity Type

Hair And Beauty

Number of Pages Required

3 page

Font styles to use
Other font styles liked:
• see my images for my current logo

Colors
000000
b2b2b2
a54499

Requirements
Must have
• Style
• Fast turnaround
• Be viewable on all devices, PC, ipads, smart phones
• Designer able to upload it so its a running website for me to my URL
Nice to have
• Just a really feminine, stylish website which is easy to read and shows some beautiful images of perfect hair
Should not have
• Browns, reds or orange colours.

```html
<!DOCTYPE html>
<html lang="en">
<head>
<meta charset="utf-8">
<title>Lune Hair &amp; Body</title>
<link href="https://fonts.googleapis.com/css2?family=Hind:wght@300;400;500;600&display=swap" rel="stylesheet">
<style>
:root{
  --purple:#a4449a;
  --purple-dark:#2b1a28;
  --plum:#4a1f42;
  --ink:#111;
  --text:#555;
  --white:#fff;
  --footer:#2a2a2a;
  --footer-deep:#1c1c1c;
  --line:#c9c9c9;
}
*{margin:0;padding:0;box-sizing:border-box}
html,body{width:1200px;height:3529px;overflow:hidden}
body{font-family:"Hind",Arial,sans-serif;color:var(--text);background:var(--white);position:relative}
.abs{position:absolute}
/* hero */
.hero{left:0;top:0;width:1200px;height:800px;background:linear-gradient(100deg,#1e0d1b 0%,#3b1536 35%,#7a2c6e 62%,#b3579f 80%,#4a1a40 100%)}
.hero-photo{left:560px;top:0;width:640px;height:800px;background:radial-gradient(ellipse at 60% 40%,#c98fb8 0%,#9a3f8c 45%,rgba(60,20,55,0) 75%)}
.topbar{left:47px;top:19px;width:1094px;height:117px;background:rgba(20,8,18,.55)}
.logo{left:72px;top:36px;color:var(--white);font-weight:300;font-size:64px;line-height:1}
.logo small{display:block;font-size:16px;letter-spacing:2px;margin:2px 0 0 40px}
.social{right:84px;top:38px;display:flex;gap:6px}
.social span{width:26px;height:26px;border-radius:50%;background:var(--white)}
.nav{right:84px;top:98px;display:flex;gap:60px;font-size:16px;color:var(--white);font-weight:500}
.nav .on{border-bottom:3px solid var(--purple);padding-bottom:10px}
.hero-title{left:57px;top:248px;color:var(--white);font-weight:500;font-size:46px}
.lead{left:63px;top:322px;width:520px;color:var(--white);font-size:14.5px;line-height:26px}
.btn-line{border:2px solid var(--white);color:var(--white);font-size:15px;text-align:center;font-weight:500}
.appt{left:63px;top:456px;width:230px;height:46px;line-height:44px}
.infobar{left:59px;top:624px;width:1082px;height:106px;background:rgba(70,50,65,.6);display:flex;align-items:center}
.info{display:flex;align-items:center;gap:16px;color:var(--white);width:360px;padding-left:22px}
.info b{display:block;font-size:15px;font-weight:600}
.info span{font-size:14px}
/* services */
.services{left:0;top:800px;width:1200px;height:228px;background:var(--purple)}
.svc{top:46px;width:200px;text-align:center;color:var(--white);font-size:19px;font-weight:500}
.svc svg{display:block;margin:0 auto 18px}
.arrow{top:100px;color:var(--white);font-size:30px}
/* reveal */
.section-title{color:var(--ink);font-weight:400;font-size:40px;text-align:center}
.sub{font-size:14.5px;color:#555;text-align:center}
.divider{width:190px;height:1px;background:var(--line)}
.reveal-text{left:75px;top:1262px;width:490px;text-align:center;font-size:14.5px;line-height:23px;color:#666}
.learn{left:223px;top:1394px;width:190px;height:50px;border:2px solid var(--purple);color:#444;font-size:15px;text-align:center;line-height:46px;font-weight:500}
.frame{left:781px;top:1120px;width:259px;height:386px;border:2px solid #555}
.reveal-img{left:744px;top:1082px;width:263px;height:398px;background:linear-gradient(160deg,#d8d3cb,#b9a88f 55%,#efece8)}
/* banner */
.banner{left:0;top:1595px;width:1200px;height:240px;background:linear-gradient(90deg,var(--purple-dark),#5a2a50 55%,var(--purple-dark))}
.banner-title{left:0;top:1628px;width:1200px;text-align:center;color:var(--white);font-weight:300;font-size:31px}
.pill{left:454px;top:1734px;width:292px;height:50px;border-radius:25px;background:var(--purple);color:var(--white);text-align:center;line-height:52px;font-size:17px;font-weight:500}
/* gallery */
.grid{left:59px;top:2017px;width:1080px;height:477px;display:grid;grid-template-columns:repeat(3,1fr);grid-template-rows:repeat(2,1fr)}
.grid div:nth-child(1){background:linear-gradient(135deg,#d4dbe3,#6b4b3a)}
.grid div:nth-child(2){background:linear-gradient(135deg,#6f8aa7,#c98b7c)}
.grid div:nth-child(3){background:linear-gradient(135deg,#f1ead9,#d9b87a)}
.grid div:nth-child(4){background:linear-gradient(135deg,#7b9c4f,#8a5a3e)}
.grid div:nth-child(5){background:linear-gradient(135deg,#4a3a33,#a0705a)}
.grid div:nth-child(6){background:linear-gradient(135deg,#050505,#c9ab82 60%,#111)}
/* prices */
.prices-photo{left:0;top:2607px;width:1200px;height:485px;background:linear-gradient(90deg,#5b6470 0%,#8f98a3 40%,#dfe3e8 65%,#eef0f2 100%)}
.pricebox{left:704px;top:2659px;width:411px;height:395px;border:2px solid var(--purple);background:rgba(232,232,236,.92);padding:24px 38px 0 38px}
.pricebox .brand{text-align:center;color:#999;font-weight:300;font-size:50px;line-height:1}
.pricebox .brand small{display:block;font-size:13px;letter-spacing:2px}
.pricebox ul{list-style:none;margin-top:42px}
.pricebox li{display:flex;font-size:17px;color:#333;height:33.5px;align-items:center}
.pricebox li i{flex:1;border-bottom:1px dashed #777;margin:0 4px;transform:translateY(-4px)}
/* contact strip */
.strip{left:0;top:3092px;width:1200px;height:108px;background:var(--purple)}
.strip-title{left:130px;top:3124px;color:var(--white);font-size:26px;font-weight:600}
.contact-btn{left:887px;top:3120px;width:254px;height:54px;line-height:54px;font-size:26px;font-weight:400}
/* footer */
.footer{left:0;top:3200px;width:1200px;height:278px;background:var(--footer)}
.footer-heading{color:var(--white);font-size:20px;font-weight:600;line-height:1.2}
.news{left:64px;top:3242px;width:290px}
.news ul{margin-top:14px}
.news li{list-style:none;color:#ddd;font-size:14px;border-bottom:1px solid #444;padding:8px 0 7px}
.open{left:414px;top:3242px}
.hours{margin-top:16px;width:328px;height:137px;border:2px solid var(--purple);padding:12px 18px}
.hours div{display:flex;justify-content:space-between;color:#ddd;font-size:14px;height:37px;align-items:center;border-bottom:1px solid #444}
.hours div:last-child{border:none}
.contact{left:812px;top:3242px;width:283px}
.contact .name{color:var(--white);font-size:14px;font-weight:600;margin:14px 0 4px;border-bottom:1px solid #444;padding-bottom:4px}
.contact .row{display:flex;color:#ddd;font-size:14px;padding:4px 0;border-bottom:1px solid #444}
.contact .row b{font-weight:400;width:80px}
.bottom{left:0;top:3478px;width:1200px;height:51px;background:var(--footer-deep);color:#ddd;font-size:14px;text-align:center;line-height:52px}
</style>
</head>
<body>

<section class="hero abs" aria-label="Hero"></section>
<div class="hero-photo abs" role="img" aria-label="Photo of a woman with long glossy violet hair and a straight fringe"></div>
<header class="topbar abs"></header>
<div class="logo abs">Lune<small>hair &amp; body</small></div>
<div class="social abs" aria-label="Social links"><span></span><span></span><span></span><span></span><span></span></div>
<nav class="nav abs"><span class="on">HOME</span><span>PRICE LIST</span><span>CONTACT US</span></nav>
<h1 class="hero-title abs">Beautiful hair, Healthy you</h1>
<p class="lead abs">"We pride ourselves on being able to offer a private salon experience to our clients in the exclusive suburb of Seabrook, where your hair design and colouring needs will be met with years of experience and current industry training and knowledge".</p>
<div class="btn-line appt abs">BY APPOINTMENT ONLY</div>

<div class="infobar abs">
  <div class="info">
    <svg width="60" height="60" viewBox="0 0 60 60"><circle cx="30" cy="30" r="26" fill="none" stroke="#fff" stroke-width="4"/><path d="M30 14v17h12" fill="none" stroke="#fff" stroke-width="4"/></svg>
    <div><b>OPENING TIMES</b><span>MONDAY – FRIDAY: 09:00 – 22:00</span></div>
  </div>
  <div class="info">
    <svg width="46" height="60" viewBox="0 0 46 60"><path d="M23 2C11 2 2 11 2 23c0 16 21 35 21 35s21-19 21-35C44 11 35 2 23 2z" fill="#fff"/><circle cx="23" cy="22" r="8" fill="#4a3a46"/></svg>
    <div><b>OUR LOCATION</b><span>100 HARBOUR LANE CENTRE, SEABROOK</span></div>
  </div>
  <div class="info">
    <svg width="60" height="60" viewBox="0 0 60 60"><rect x="3" y="9" width="54" height="48" fill="none" stroke="#fff" stroke-width="4"/><rect x="3" y="9" width="54" height="12" fill="#fff"/><path d="M14 3v12M46 3v12" stroke="#fff" stroke-width="4"/><g fill="#fff"><rect x="11" y="27" width="8" height="7"/><rect x="26" y="27" width="8" height="7"/><rect x="41" y="27" width="8" height="7"/><rect x="11" y="40" width="8" height="7"/><rect x="26" y="40" width="8" height="7"/><rect x="41" y="40" width="8" height="7"/></g></svg>
    <div><b>BOOK NOW</b><span>+61 8 5550 4172</span></div>
  </div>
</div>

<section class="services abs" aria-label="Services">
  <div class="arrow abs" style="left:14px">‹</div>
  <div class="svc abs" style="left:13px">
    <svg width="90" height="90" viewBox="0 0 90 90"><path d="M8 20h50c10 0 18 8 18 18s-8 18-18 18H40l-6 30H22l4-30H8z" fill="#fff"/><circle cx="58" cy="38" r="8" fill="#a4449a"/></svg>BLOW OUTS</div>
  <div class="svc abs" style="left:241px">
    <svg width="90" height="90" viewBox="0 0 90 90"><path d="M14 48h62c0 18-14 30-31 30S14 66 14 48z" fill="#fff"/><path d="M40 44 60 6l6 4-20 34z" fill="#fff"/></svg>COLOR</div>
  <div class="svc abs" style="left:474px">
    <svg width="90" height="90" viewBox="0 0 90 90"><circle cx="45" cy="45" r="40" fill="#fff"/><circle cx="34" cy="60" r="8" fill="none" stroke="#a4449a" stroke-width="4"/><circle cx="56" cy="60" r="8" fill="none" stroke="#a4449a" stroke-width="4"/><path d="M38 54 58 18M52 54 32 18" stroke="#a4449a" stroke-width="4"/></svg>CUTS</div>
  <div class="svc abs" style="left:705px">
    <svg width="90" height="90" viewBox="0 0 90 90"><path d="M20 80c0-40 10-70 40-70 18 0 22 16 22 30" fill="none" stroke="#fff" stroke-width="8"/><path d="M36 80c0-30 6-50 24-50M52 80c0-18 4-30 14-30" fill="none" stroke="#fff" stroke-width="6"/></svg>KERATIN</div>
  <div class="svc abs" style="left:945px">
    <svg width="90" height="90" viewBox="0 0 90 90"><rect x="22" y="48" width="46" height="36" rx="8" fill="#fff"/><rect x="38" y="30" width="14" height="18" fill="#fff"/><path d="M50 32 82 8" stroke="#fff" stroke-width="8"/></svg>GEL MANICURES</div>
  <div class="arrow abs" style="left:1158px">›</div>
</section>

<section class="reveal" aria-label="About">
  <h2 class="section-title abs" style="left:60px;top:1126px;width:520px">REVEAL YOUR BEAUTY</h2>
  <div class="sub abs" style="left:60px;top:1193px;width:520px">BOOK AN APPOINTMENT AND WE'LL TAKE CARE OF THE REST</div>
  <div class="divider abs" style="left:225px;top:1244px"></div>
  <p class="reveal-text abs">Duis autem vel eum iriure dolor in hendrerit in putate velit esse molestie consequat, vel illum doloreeu feugiatDuis autem vel eum iriure dolor in hendrerit in putate velit esse molestie consequat, vel illum doloreeu feugiat</p>
  <div class="learn abs">LEARN MORE</div>
  <div class="frame abs"></div>
  <div class="reveal-img abs" role="img" aria-label="Smiling blonde make-up artist holding a fan of brushes"></div>
</section>

<section class="banner abs" role="img" aria-label="Dim plum backdrop with a woman's hair"></section>
<h3 class="banner-title abs">We can provide full service Hair &amp; Beauty Bar</h3>
<div class="divider abs" style="left:505px;top:1690px;background:#8a6a84"></div>
<div class="pill abs">Our Pricing List</div>

<section class="gallery" aria-label="Gallery">
  <h2 class="section-title abs" style="left:0;top:1900px;width:1200px">Our Gallery</h2>
  <div class="divider abs" style="left:505px;top:1982px"></div>
  <div class="grid abs">
    <div role="img" aria-label="Woman with long dark wavy hair"></div>
    <div role="img" aria-label="Woman with retro pin-up styled hair and headscarf"></div>
    <div role="img" aria-label="Woman with voluminous blonde curls"></div>
    <div role="img" aria-label="Woman with long brown hair outdoors"></div>
    <div role="img" aria-label="Woman with auburn hair against wood backdrop"></div>
    <div role="img" aria-label="Woman with blonde waves on black backdrop"></div>
  </div>
</section>

<section class="prices-photo abs" role="img" aria-label="Bearded man with glasses in a denim shirt"></section>
<div class="pricebox abs">
  <div class="brand">Lune<small>hair &amp; body</small></div>
  <ul>
    <li>Haircut<i></i>$40</li>
    <li>Beard Trim<i></i>$25</li>
    <li>Flat Top<i></i>$45</li>
    <li>Hairstyle<i></i>$50</li>
    <li>Hot Shave<i></i>$20</li>
    <li>Outline<i></i>$35</li>
    <li>Line Up<i></i>$30</li>
  </ul>
</div>

<section class="strip abs" aria-label="Offers"></section>
<svg class="abs" style="left:59px;top:3121px" width="52" height="52" viewBox="0 0 52 52"><circle cx="26" cy="26" r="23" fill="none" stroke="#fff" stroke-width="3"/><path d="M17 14c-3 3-2 9 4 16s12 9 15 6l2-3-6-5-3 2c-3-1-6-4-7-7l2-3-5-6z" fill="#fff"/></svg>
<h4 class="strip-title abs">Contact us now and get special offers!</h4>
<div class="btn-line contact-btn abs">Contact Form</div>

<footer class="footer abs"></footer>
<div class="news abs">
  <h5 class="footer-heading">Latest News</h5>
  <ul>
    <li>How to Make Your Hair Grow Faster</li>
    <li>5 Ways to Make Hair Look Gorgeous</li>
    <li>14 Easy Ways to Get Standout Eyes</li>
    <li>An Owner's Guide to Naturally Wavy Hair</li>
  </ul>
</div>
<div class="open abs">
  <h5 class="footer-heading">We're Open</h5>
  <div class="hours">
    <div><span>Monday - Friday</span><span>9 am to 10 pm</span></div>
    <div><span>Monday - Friday</span><span>9 am to 12 pm</span></div>
    <div><span>Monday - Friday</span><span>8 am to 12 pm</span></div>
  </div>
</div>
<div class="contact abs">
  <h5 class="footer-heading">Contact Us</h5>
  <div class="name">LUNE HAIR</div>
  <div class="row"><b>Phone:</b>0400 555 218</div>
  <div class="row"><b>Fax:</b>0400 555 934</div>
  <div class="row"><b>Email:</b>hello@lune-salon.com</div>
  <div class="row"><b>Web:</b>http://www.lunetresses.com.au/</div>
</div>
<div class="bottom abs">www.lunetresses.com.au - SEABROOK, Western Australia - 6999 - By Appointment Only</div>

</body>
</html>
```